GRAPHIC DESIGN FOR RESTAURANT MENU FOR HEALTHY RESTAURANT

I am looking for a graphic design for our menu displayed on a TV screen. Please ensure the file will fit on a TV screen nicely. We are looking for a clean design , with the following items. We would also like to include a couple of photos.
Breakfast:
Protein Chocolate Chip Pancakes - $12.95
Sunny Trail Burrito- $11.95
Tall Barn Omelette - $12.95
Lunch
Butter Chicken - $13.95
Chicken Quesadilla - $13.45
Coconut Garlic Shrimp - $15.95
Goat Cheese Stuffed Chicken - $14.95
Chipotle Steak Wrap - $12.95
Turkey Meatball Fettuccini - $13.45
Chicken Alfredo - $13.45
Chicken Parmesan - $13.95
Pesto Chicken Pasta - $13.45
Steak Bite and Green Stir Fry - $13.45
Asian Chicken Teriyaki - $13.45
Please include our logo
Restaurant

```html
<!DOCTYPE html>
<html lang="en">
<head>
<meta charset="utf-8">
<title>Freshwell Menu Board</title>
<link href="https://fonts.googleapis.com/css2?family=Noto+Sans:wght@400;700&family=Roboto:wght@700&display=swap" rel="stylesheet">
<style>
  :root {
    --green: #8dc21f;
    --green-soft: rgba(141, 194, 31, 0.55);
    --green-fade: rgba(141, 194, 31, 0);
    --text-grey: #6b6b6b;
    --band-grey: #e9eaeb;
    --white: #ffffff;
  }
  html, body {
    margin: 0;
    padding: 0;
    width: 1200px;
    height: 681px;
    overflow: hidden;
    background: var(--white);
  }
  .menu-board {
    position: relative;
    width: 1200px;
    height: 681px;
    overflow: hidden;
    background: var(--white);
    font-family: "Noto Sans", Arial, sans-serif;
  }
  .bottom-band {
    position: absolute;
    left: 0;
    top: 0;
    width: 1200px;
    height: 681px;
  }
  .brand {
    position: absolute;
    left: 46px;
    top: 76px;
    width: 320px;
  }
  .brand-name {
    margin: 0;
    font-family: "Roboto", Arial, sans-serif;
    font-weight: 700;
    font-size: 54px;
    line-height: 1;
    letter-spacing: 1px;
    color: var(--green);
  }
  .brand-tagline {
    margin: 6px 0 0 8px;
    font-family: "Roboto", Arial, sans-serif;
    font-weight: 700;
    font-size: 19px;
    color: var(--green);
    white-space: nowrap;
  }
  .brand-tagline .divider {
    display: inline-block;
    width: 2px;
    height: 20px;
    margin: 0 10px -3px;
    background: var(--green);
  }
  .menu-section {
    position: absolute;
  }
  .menu-section h2 {
    margin: 0;
    font-weight: 700;
    font-size: 29px;
    line-height: 1;
    color: var(--green);
    letter-spacing: 0.5px;
  }
  .breakfast { left: 446px; top: 80px; width: 310px; }
  .lunch { left: 855px; top: 80px; width: 250px; }
  .menu-list {
    list-style: none;
    margin: 0;
    padding: 0;
    position: relative;
  }
  .menu-item {
    position: absolute;
    left: 2px;
    width: 100%;
    font-size: 13.5px;
    line-height: 18px;
    color: var(--text-grey);
  }
  .menu-item .price {
    position: absolute;
    top: 0;
    font-weight: 700;
    color: var(--green);
  }
  .breakfast .price { left: 252px; }
  .lunch .price { left: 197px; }
  .photo {
    position: absolute;
  }
  .photo-pasta {
    left: 1025px; top: -6px; width: 180px; height: 120px;
    border-radius: 50%;
    background: radial-gradient(ellipse at 55% 45%, #d9462a 0%, #c94a2c 35%, #e8d6c8 62%, #f4f4f4 75%);
  }
  .photo-pancakes {
    left: 416px; top: 337px; width: 288px; height: 132px;
    border-radius: 6px;
    background: radial-gradient(ellipse at 50% 45%, #d8b48a 0%, #b98a5c 30%, #e6e6e6 60%, #f5f5f5 80%);
  }
  .photo-wrap {
    left: 393px; top: 496px; width: 413px; height: 185px;
    border-radius: 40% 40% 0 0;
    background: radial-gradient(ellipse at 55% 50%, #8a6a4a 0%, #c9ac88 35%, #dcc6a8 60%, rgba(233,234,235,0) 85%);
  }
  .photo-omelette {
    left: -6px; top: 390px; width: 310px; height: 246px;
    border-radius: 0 30px 30px 0;
    background: radial-gradient(ellipse at 35% 60%, #f2c23a 0%, #e8b23a 35%, #a57a4e 55%, #eeeeee 75%);
  }
  .leaf-area {
    position: absolute;
    border-radius: 50%;
    background: radial-gradient(ellipse at center, var(--green-soft) 0%, var(--green-fade) 70%);
  }
  .leaf-area-top { left: 0; top: 215px; width: 350px; height: 180px; }
  .leaf-area-bottom { left: 100px; top: 480px; width: 380px; height: 210px; }
</style>
</head>
<body>
<main class="menu-board">
  <svg class="bottom-band" viewBox="0 0 1200 681" aria-hidden="true">
    <path d="M0 566 C300 590 700 630 1000 642 C1150 648 1190 625 1200 600 L1200 681 L0 681 Z" fill="var(--band-grey)"/>
  </svg>

  <header class="brand">
    <h1 class="brand-name">FRESHWELL</h1>
    <p class="brand-tagline">HEALTHY KITCHEN<span class="divider"></span>MEAL PREP</p>
  </header>

  <div class="leaf-area leaf-area-top" role="img" aria-label="Scattered falling green leaves"></div>

  <div class="photo photo-omelette" role="img" aria-label="Photo of an omelette with whole-grain toast on a white plate"></div>
  <div class="photo photo-pancakes" role="img" aria-label="Photo of stacked chocolate chip pancakes with banana on a square plate"></div>
  <div class="photo photo-wrap" role="img" aria-label="Photo of a steak and vegetable wrap cut in half"></div>
  <div class="photo photo-pasta" role="img" aria-label="Photo of a bowl of turkey meatball fettuccine"></div>

  <div class="leaf-area leaf-area-bottom" role="img" aria-label="Large green leaves"></div>

  <section class="menu-section breakfast">
    <h2>BREAKFAST</h2>
    <ul class="menu-list">
      <li class="menu-item" style="top:31px">Protein Chocolate Chip Pancakes<span class="price">$12.95</span></li>
      <li class="menu-item" style="top:80px">Sunny Trail Burrito<span class="price">$11.95</span></li>
      <li class="menu-item" style="top:130px">Tall Barn Omelette<span class="price">$12.95</span></li>
    </ul>
  </section>

  <section class="menu-section lunch">
    <h2>LUNCH</h2>
    <ul class="menu-list">
      <li class="menu-item" style="top:31px">Butter Chicken<span class="price">$13.95</span></li>
      <li class="menu-item" style="top:75px">Chicken Quesadilla<span class="price">$13.45</span></li>
      <li class="menu-item" style="top:119px">Coconut Garlic Shrimp<span class="price">$15.95</span></li>
      <li class="menu-item" style="top:163px">Goat Cheese Stuffed Chicken<span class="price">$14.95</span></li>
      <li class="menu-item" style="top:207px">Chipotle Steak Wrap<span class="price">$12.95</span></li>
      <li class="menu-item" style="top:251px">Turkey Meatball Fettuccini<span class="price">$13.45</span></li>
      <li class="menu-item" style="top:295px">Chicken Alfredo<span class="price">$13.45</span></li>
      <li class="menu-item" style="top:339px">Chicken Parmesan<span class="price">$13.95</span></li>
      <li class="menu-item" style="top:383px">Pesto Chicken Pasta<span class="price">$13.45</span></li>
      <li class="menu-item" style="top:427px">Steak Bite and Green Stir Fry<span class="price">$13.45</span></li>
      <li class="menu-item" style="top:471px">Asian Chicken Teriyaki<span class="price">$13.45</span></li>
    </ul>
  </section>
</main>
</body>
</html>
```